Real Estate Seller Financing Postcard

I need a postcard that lays out these options contained in the notes that grabs attention, explains the two options easily and is eye-catching. The front needs to have the percentages on it and information about it and on the other side One side exact Text is:
"Monthly income without tenant headaches" in big letters. Also on front "Get
110%
add an "or"
160% of market value for your property. ". The percentages should be displayed and that is not to be a sentence of text. Other side text: I need bullets points for these "Formal protection as a lien holder against home
No commission or closing cost
Fast closings possible
Property taken as is so no repairs.

Add to the top of the back in "It’s simple. I am a new investor without down payment capital who still want to double our portfolio this year to grow our portfolio."
Here are the two options that are to be the largest part of the back
Option 1, you can receive 80% now cash and 30% over a short period of time including interest.

Option 2, where act like a bank allowing you to make 150% if you finance the whole property(ies). No gimmicks and surprises, just simple unconventional financing.

Include Logo Somewhere

Target Market(s)

Property Owners Wanting to Sell Their Property

Industry/Entity Type

Real Estate Investing

Requirements
Must have
• The options promiment and each side with its respective information. Must have logo somewhere
Nice to have
• The options in color other than black.
Should not have
• A picture of money on the front. Any other image is okay.

```html
<!DOCTYPE html>
<html lang="en">
<head>
<meta charset="utf-8">
<title>Northgate Real Estate Group – Seller Financing Postcard</title>
<link rel="stylesheet" href="https://fonts.googleapis.com/css2?family=Ubuntu:wght@400;500;700&family=Dancing+Script:wght@500&display=swap">
<style>
  :root{
    --backdrop:#1f3f8a;
    --brand-blue:#1f3f8a;
    --slate:#5f5f5f;
    --ink:#3c3c3c;
    --white:#ffffff;
    --paper-a:#f4f4f4;
    --paper-b:#e2e2e2;
    --rule:#8a8a8a;
  }
  *{margin:0;padding:0;box-sizing:border-box}
  html,body{width:851px;height:1200px;overflow:hidden}
  body{background:var(--backdrop);font-family:"Ubuntu",sans-serif;position:relative}
  .card{position:absolute;left:72px;width:710px;overflow:hidden;box-shadow:4px 6px 10px rgba(0,0,0,.45)}
  .abs{position:absolute}

  /* front */
  .front{top:61px;height:519px;background:var(--slate)}
  .front-intro{left:0;top:0;width:279px;height:415px;background:linear-gradient(90deg,#ececec,#ffffff 55%,#e6e6e6)}
  .front-contact{left:0;top:415px;width:279px;height:104px;background:var(--brand-blue);color:var(--white);text-align:center}
  .front-contact .phone{margin-top:18px;font-size:22px;font-weight:500;letter-spacing:.5px}
  .front-contact .web{margin-top:9px;font-size:15px;font-weight:500}
  .brand{display:flex;align-items:center;gap:8px;color:var(--brand-blue);font-weight:500}
  .brand-mark{width:52px;height:52px;border:2px solid var(--brand-blue);border-radius:50%;flex:none}
  .brand-name{font-size:27px;line-height:1;letter-spacing:.5px}
  .brand-sub{font-size:12px;line-height:1.3;letter-spacing:.3px}
  .front .brand{left:30px;top:19px}
  .headline{left:30px;top:119px;font-size:34px;font-weight:500;line-height:44px;letter-spacing:.3px}
  .headline .accent{color:var(--brand-blue);display:block}
  .headline .muted{color:var(--slate);display:block}
  .offer-title{left:279px;width:431px;top:22px;text-align:center;color:var(--white);font-size:56px;font-weight:700}
  .offer-box{top:127px;width:117px;height:90px;border:4px solid var(--white);color:var(--white);display:flex;align-items:center;justify-content:center;font-size:35px;font-weight:500}
  .offer-box sup{font-size:14px;font-weight:700;margin-left:1px;position:relative;top:-4px}
  .offer-note{left:279px;width:431px;top:246px;text-align:center;color:var(--white);font-size:22px;line-height:29px}
  .photo{left:279px;top:300px;width:431px;height:260px;background:radial-gradient(ellipse at 55% 50%,#c9a58f 0%,#8a7468 22%,#5f5f5f 55%)}

  /* back */
  .back{top:612px;height:514px;background:linear-gradient(180deg,var(--paper-a),var(--white) 40%,var(--paper-b))}
  .simple-title{left:41px;top:26px;font-family:"Dancing Script",cursive;font-size:37px;color:var(--brand-blue)}
  .simple-rule{left:211px;top:27px;width:1px;height:47px;background:var(--rule)}
  .simple-text{left:230px;top:28px;width:345px;font-size:14.5px;line-height:19px;color:var(--ink)}
  .stamp{left:594px;top:32px;width:80px;height:80px;border:1.5px solid var(--brand-blue)}
  .option{top:117px;width:174px;height:171px;border:6px solid var(--slate);background:#ececec;text-align:center;padding:12px 4px 0}
  .option h2{font-size:24px;font-weight:500;color:var(--slate);margin-bottom:14px}
  .option p{font-size:13.5px;line-height:18.5px;color:var(--ink)}
  .option.featured{left:235px;border-color:var(--brand-blue);background:#f5f5f5}
  .option.featured h2,.option.featured p{color:var(--brand-blue)}
  .option.featured p{font-weight:500;font-size:13px;letter-spacing:-.1px}
  .address-line{left:508px;width:166px;height:1.5px;background:var(--rule)}
  .back .brand{left:506px;top:295px;gap:6px}
  .back .brand-mark{width:44px;height:44px}
  .back .brand-name{font-size:22px}
  .back .brand-sub{font-size:10.5px}
  .tagline{left:37px;top:324px;font-size:14.5px;color:var(--ink)}
  .benefits{left:0;top:356px;width:710px;height:102px;background:var(--slate);display:flex;color:var(--white);list-style:none}
  .benefit{flex:1;text-align:center;font-size:14px;line-height:18px;padding-top:12px;position:relative}
  .benefit+.benefit::before{content:"";position:absolute;left:0;top:26px;width:1px;height:50px;background:#9a9a9a}
  .benefit svg{display:block;margin:0 auto 8px}
  .footer{left:0;top:458px;width:710px;height:56px;background:var(--brand-blue);color:var(--white);font-size:15px;font-weight:500}
  .footer span{position:absolute;top:18px;white-space:nowrap}
  .footer .email{left:36px}
  .footer .site{left:349px;transform:translateX(-50%)}
  .footer .phone{right:40px}
</style>
</head>
<body>

<section class="card front">
  <div class="abs front-intro">
    <div class="abs brand">
      <span class="brand-mark"></span>
      <div><div class="brand-name">NORTHGATE</div><div class="brand-sub">REAL ESTATE GROUP</div></div>
    </div>
    <h1 class="abs headline">
      <span class="accent">WANT</span>
      <span class="accent">MONTHLY</span>
      <span class="accent">INCOME</span>
      <span class="muted">WITHOUT</span>
      <span class="muted">TENANT</span>
      <span class="muted">HEADACHES?</span>
    </h1>
  </div>
  <div class="abs front-contact">
    <div class="phone">Ph : 0198 455 2710</div>
    <div class="web">northgatehomes.com</div>
  </div>

  <div class="abs photo" role="img" aria-label="Photo of two business people in suits shaking hands"></div>
  <div class="abs offer-title">GET</div>
  <div class="abs offer-box" style="left:298px">100<sup>%</sup></div>
  <div class="abs offer-box" style="left:431px">110<sup>%</sup></div>
  <div class="abs offer-box" style="left:564px">160<sup>%</sup></div>
  <p class="abs offer-note">of market value<br>for your property.</p>
</section>

<section class="card back">
  <div class="abs simple-title">It’s simple</div>
  <div class="abs simple-rule"></div>
  <p class="abs simple-text">I am a new investor without down payment capital who still want to double our portfolio this year to grow our portfolio.</p>
  <div class="abs stamp"></div>

  <div class="abs option" style="left:41px">
    <h2>Option 1</h2>
    <p>you can receive 80%<br>now cash and 30% over<br>a short period of time<br>including interest.</p>
  </div>
  <div class="abs option featured">
    <h2>Option 2</h2>
    <p>where act like a bank<br>allowing you to make<br>150% if you finance the<br>whole property(ies).</p>
  </div>

  <div class="abs address-line" style="top:183px"></div>
  <div class="abs address-line" style="top:221px"></div>
  <div class="abs address-line" style="top:258px"></div>

  <div class="abs brand">
    <span class="brand-mark"></span>
    <div><div class="brand-name">NORTHGATE</div><div class="brand-sub">REAL ESTATE GROUP</div></div>
  </div>
  <p class="abs tagline">No gimmicks and surprises, just simple unconventional financing.</p>

  <ul class="abs benefits">
    <li class="benefit">
      <svg width="28" height="30" viewBox="0 0 28 30" fill="none" stroke="#fff" stroke-width="1.6"><path d="M14 2 L25 6 V14 C25 21 20 26 14 28 C8 26 3 21 3 14 V6 Z"/><path d="M9 15 L13 19 L20 11"/></svg>
      Formal protection as a<br>lien holder against home
    </li>
    <li class="benefit">
      <svg width="30" height="30" viewBox="0 0 30 30" fill="none" stroke="#fff" stroke-width="1.6"><circle cx="15" cy="15" r="13"/><path d="M10 21 L20 9"/><circle cx="10.5" cy="10.5" r="2"/><circle cx="19.5" cy="19.5" r="2"/></svg>
      No commission<br>or closing cost
    </li>
    <li class="benefit">
      <svg width="30" height="30" viewBox="0 0 30 30" fill="none" stroke="#fff" stroke-width="1.6"><circle cx="15" cy="16" r="12"/><path d="M15 9 V16 L20 19"/><path d="M11 2 H19"/></svg>
      Fast closings<br>possible
    </li>
    <li class="benefit">
      <svg width="30" height="30" viewBox="0 0 30 30" fill="none" stroke="#fff" stroke-width="1.6"><path d="M3 14 L15 3 L27 14"/><path d="M6 12 V27 H24 V12"/><path d="M11 19 L14 22 L19 16"/></svg>
      Property taken as<br>is so no repairs.
    </li>
  </ul>

  <div class="abs footer">
    <span class="email">hello@northgatehomes.com</span>
    <span class="site">northgatehomes.com</span>
    <span class="phone">Ph : 0198 455 2710</span>
  </div>
</section>

</body>
</html>
```